Business card for Crestline Bathrooms

Please design a business card for our bathroom renovation business. You can use my existing logo, but if you have an idea to modernize it, I would like to see it. Please see attached files first. I would like to use the blue and the orange theme. I like the concept of using the shower head in the logo. Please find following a design (or two) that I have been trying to create with my limited resources. That design was for a sign, but I was going to adopt it and use it as a business card as well. I like the concept of the water splash but I don’t think it “flows” nicely together with the logo. Another thought is that maybe creating the logo out of water splash could work and have a dramatic effect (like the water text and the butterfly picture attached with similar background instead of white). If the above doesn’t work I would like to see a modern simplified design. One of the attached files named as the unwanted business card has all the details that I want included in the business card. Please note that it is two sided.
Updates

I am very thankful for the designs that I have received, but they are very similar and only a couple of attempts to do something with the water splash as per my original brief. Modernizing the logo and having it made out of out of water splash with the orange as color accent could work and have a dramatic effect (like the water text and the butterfly picture attached with similar background instead of white). Please do not use the butterfly itself! This is just an example that images can be created out of water splash.

Contact Information for Business Card

all the details are on the unwonted business card file included

Colors
3176b5

Requirements
Nice to have
• Copied from the brief:
• ... maybe creating the logo out of water splash could work and have a dramatic effect (like the water text and the butterfly picture attached with similar background instead of white). Please do not use the butterfly itself!
Should not have
• I am getting designs with a butterfly. The butterfly picture was an example of creating something from a water splash. The butterfly itself has no association with anything other than the concept of creating a logo out of water splash. Sorry, I thought I was clear in the brief.

```html
<!DOCTYPE html>
<html lang="en">
<head>
<meta charset="UTF-8">
<title>Crestline Bathrooms – Business Card</title>
<link href="https://fonts.googleapis.com/css2?family=Roboto+Condensed:wght@700&display=swap" rel="stylesheet">
<style>
  :root {
    --page-bg: #e9edf2;
    --card-blue: #3176b5;
    --card-deep: #1d4f86;
    --card-light: #5c96cc;
    --ink-dark: #0c1a2b;
    --ink-light: #ffffff;
    --splash-light: #8fbbe3;
    --accent: #f28a1e;
  }
  * { margin: 0; padding: 0; box-sizing: border-box; }
  html, body {
    width: 1200px; height: 1200px; overflow: hidden;
    background: var(--page-bg);
    font-family: "Roboto Condensed", "Arial Narrow", sans-serif;
  }
  .sheet {
    width: 1200px; height: 1200px;
    display: flex; flex-direction: column; align-items: center; justify-content: center;
    gap: 60px;
  }
  .card {
    position: relative;
    width: 840px; height: 480px;
    border-radius: 22px;
    overflow: hidden;
    background: linear-gradient(135deg, var(--card-light) 0%, var(--card-blue) 45%, var(--card-deep) 100%);
    box-shadow: 0 10px 28px rgba(20, 40, 70, 0.22);
  }
  .droplets { position: absolute; inset: 0; }

  /* Front side */
  .front .brand {
    position: absolute; left: 70px; top: 120px;
    display: flex; align-items: center; gap: 18px;
  }
  .brand-dot {
    width: 22px; height: 22px; border-radius: 50%;
    background: var(--accent);
  }
  .brand-name {
    color: var(--ink-light);
    font-weight: 700; font-size: 58px; letter-spacing: 1px;
    line-height: 1;
  }
  .front .person {
    position: absolute; left: 70px; bottom: 110px;
  }
  .person-name {
    color: var(--ink-dark);
    font-weight: 700; font-size: 40px; letter-spacing: 1px;
    text-transform: uppercase;
  }
  .person-rule {
    margin-top: 14px; width: 420px; height: 4px;
    background: var(--ink-dark);
  }

  /* Back side */
  .back .splash {
    position: absolute; left: 0; top: 0; width: 840px; height: 190px;
  }
  .back .services {
    position: absolute; left: 60px; top: 40px; right: 60px;
    color: var(--ink-dark);
  }
  .services-title {
    font-size: 28px; letter-spacing: 2px; text-align: center;
    margin-left: 160px; margin-bottom: 16px;
  }
  .services-list { list-style: none; }
  .services-list li {
    font-size: 30px; line-height: 1.28; letter-spacing: 0.5px;
    display: flex; align-items: center; gap: 12px;
  }
  .services-list li::before {
    content: ""; width: 0; height: 0;
    border-top: 7px solid transparent; border-bottom: 7px solid transparent;
    border-left: 11px solid var(--ink-dark);
  }
  .back .rules {
    position: absolute; left: 0; right: 0; top: 292px;
  }
  .rule { height: 4px; background: var(--ink-dark); }
  .rule + .rule { margin-top: 10px; }
  .rule-gap { height: 40px; }
  .back .brand {
    position: absolute; right: 70px; bottom: 36px;
    display: flex; align-items: center; gap: 14px;
  }
  .back .brand-name { font-size: 44px; }
  .back .brand-dot { width: 18px; height: 18px; }
</style>
</head>
<body>
<main class="sheet">

  <section class="card front" aria-label="Business card front">
    <svg class="droplets" width="840" height="480" aria-hidden="true">
      <g fill="rgba(255,255,255,0.35)">
        <circle cx="640" cy="90" r="4"/><circle cx="700" cy="150" r="3"/>
        <circle cx="760" cy="240" r="4"/><circle cx="610" cy="300" r="3"/>
        <circle cx="720" cy="380" r="3"/><circle cx="520" cy="420" r="4"/>
        <circle cx="790" cy="60" r="3"/><circle cx="560" cy="220" r="3"/>
      </g>
    </svg>
    <div class="brand">
      <span class="brand-dot"></span>
      <span class="brand-name">Crestline Bathrooms</span>
    </div>
    <div class="person">
      <p class="person-name">Daniel Marsh</p>
      <div class="person-rule"></div>
    </div>
  </section>

  <section class="card back" aria-label="Business card back">
    <svg class="splash" viewBox="0 0 840 190" role="img" aria-label="Water splash background image">
      <defs>
        <linearGradient id="splashTone" x1="0" y1="0" x2="1" y2="1">
          <stop offset="0" stop-color="var(--splash-light)" stop-opacity="0.55"/>
          <stop offset="1" stop-color="var(--card-blue)" stop-opacity="0"/>
        </linearGradient>
      </defs>
      <rect width="840" height="190" fill="url(#splashTone)"/>
    </svg>
    <svg class="droplets" width="840" height="480" aria-hidden="true">
      <g fill="rgba(255,255,255,0.3)">
        <circle cx="150" cy="440" r="4"/><circle cx="320" cy="400" r="3"/>
        <circle cx="420" cy="450" r="3"/><circle cx="90" cy="380" r="3"/>
        <circle cx="240" cy="460" r="3"/>
      </g>
    </svg>
    <div class="services">
      <h2 class="services-title">SERVICES</h2>
      <ul class="services-list">
        <li>COMPLETE BATHROOM RENOVATIONS &amp; REMODELLING</li>
        <li>HIGHLY SKILLED &amp; QUALIFIED TRADESPEOPLE</li>
        <li>PROFESSIONAL SERVICE FROM CONCEPT TO COMPLETION</li>
        <li>ALL WORK GUARANTEED</li>
      </ul>
    </div>
    <div class="rules" aria-hidden="true">
      <div class="rule"></div><div class="rule"></div>
      <div class="rule-gap"></div>
      <div class="rule"></div><div class="rule"></div>
    </div>
    <div class="brand">
      <span class="brand-dot"></span>
      <span class="brand-name">Crestline Bathrooms</span>
    </div>
  </section>

</main>
</body>
</html>
```